update of B2B website and conversion to single page

The current website needs to be modernized. I want what is commonly called a single page website. It is not actually a single page. See some examples here:
https://www.brivane.example/
https://www.quorel.example/
https://www.tindlewick.example/
Most or all graphics will be replaced.
Please see the attached spreadsheet for a rough draft of the home page layout. Convert the existing website at https://www.zolvinbyte.example/ to a single page website. We will provide the page content. You will provide all of the design, graphics, development, production deployment. etc. The look and feel should be corporate, polished, premium.

```html
<!DOCTYPE html>
<html lang="en">
<head>
<meta charset="utf-8">
<title>Zolvin Data — Enterprise Data Quality Made Easy</title>
<link href="https://fonts.googleapis.com/css2?family=Poppins:wght@400;500;600;700&display=swap" rel="stylesheet">
<style>
:root{
  --navy:#1b2a6b;
  --navy-dark:#13205a;
  --ink:#333333;
  --muted:#666666;
  --light-bg:#f2f2f2;
  --footer-bg:#2b2b2b;
  --accent:#f5b21b;
  --white:#ffffff;
}
*{margin:0;padding:0;box-sizing:border-box}
html,body{width:1200px;height:2403px;overflow:hidden}
body{font-family:'Poppins',sans-serif;color:var(--ink);background:var(--white);position:relative}
.abs{position:absolute}
ul{list-style:none}

/* Header */
.site-header{position:absolute;top:0;left:0;width:1200px;height:96px;background:var(--white)}
.brand{position:absolute;left:118px;top:22px;display:flex;align-items:center;gap:12px}
.brand-dot{width:40px;height:40px;border-radius:50%;background:var(--navy)}
.brand-name{font-size:30px;font-weight:600;color:var(--navy);line-height:1}
.main-nav{position:absolute;top:38px;left:0;width:1200px;font-size:15px;color:var(--ink)}
.main-nav a{position:absolute;transform:translateX(-50%);white-space:nowrap;color:inherit;text-decoration:none}

/* Hero */
.hero{position:absolute;top:96px;left:0;width:1200px;height:601px}
.hero-bg{position:absolute;inset:0;background:radial-gradient(ellipse at 50% 40%,#3b6fa8 0%,#1e4377 45%,#0c1d3d 100%)}
.hero-title{position:absolute;top:212px;width:1200px;text-align:center;color:var(--white);font-size:62px;font-weight:600}
.hero-sub{position:absolute;top:302px;width:1200px;text-align:center;color:var(--white);font-size:22px;font-weight:600;line-height:34px}
.slider-arrow{position:absolute;width:48px;height:48px;border-radius:50%;display:flex;align-items:center;justify-content:center}
.slider-arrow.prev{left:62px;top:276px;background:rgba(200,205,215,.75)}
.slider-arrow.next{left:1089px;top:276px;background:#111}

/* Time cards */
.stat-card{position:absolute;top:599px;width:309px;height:252px;background:var(--white);box-shadow:0 4px 14px rgba(0,0,0,.18);text-align:center}
.stat-card svg{position:absolute;left:94px;top:34px}
.stat-card p{position:absolute;top:150px;width:100%;font-size:22px;font-weight:500;color:#555;line-height:34px}

/* Service split */
.service{position:absolute;top:947px;height:428px}
.service-bg{position:absolute;inset:0}
.service.quality{left:0;width:596px}
.service.quality .service-bg{background:radial-gradient(ellipse at 60% 50%,#2a3440 0%,#0b0d12 75%)}
.service.mdm{left:602px;width:598px}
.service.mdm .service-bg{background:radial-gradient(ellipse at 55% 60%,#3a5e8e 0%,#15305a 55%,#0a1a36 100%)}
.service h2{position:absolute;top:118px;left:110px;color:var(--white);font-size:32px;font-weight:600}
.service.mdm h2{left:80px}
.service ul{position:absolute;top:186px;left:110px;color:var(--white);font-size:16px}
.service.mdm ul{left:80px}
.service li{display:flex;align-items:center;gap:12px;height:37px}

/* Connectors */
.connectors{position:absolute;top:1375px;left:0;width:1200px;height:471px;background:var(--light-bg)}
.connectors h2{position:absolute;top:60px;width:1200px;text-align:center;font-size:35px;font-weight:600;color:var(--navy)}
.connector-card-bg{position:absolute;left:609px;top:136px;width:231px;height:285px;background:var(--white);box-shadow:0 2px 8px rgba(0,0,0,.08)}
.connector{position:absolute;top:161px;width:220px}
.connector .icon{width:84px;height:84px;border-radius:50%;background:var(--navy);margin:0 auto;display:flex;align-items:center;justify-content:center}
.connector h3{text-align:center;font-size:19px;font-weight:400;color:#444;margin-top:13px}
.connector ul{margin-top:10px;font-size:15.5px;color:var(--muted)}
.connector li{display:flex;align-items:center;gap:10px;height:26px}
.carousel-dot{position:absolute;top:1634px;width:26px;height:26px;border-radius:50%;display:flex;align-items:center;justify-content:center}
.carousel-dot.prev{left:79px;background:#777}
.carousel-dot.next{left:1097px;background:#111}

/* CTA */
.cta{position:absolute;top:1846px;left:0;width:1200px;height:149px;background:var(--white)}
.cta p{position:absolute;left:157px;top:29px;width:560px;font-size:19px;line-height:34px;color:var(--muted)}
.cta-button{position:absolute;left:753px;top:33px;width:277px;height:56px;border-radius:28px;background:var(--navy);color:var(--white);font-size:20px;font-weight:500;display:flex;align-items:center;justify-content:center;gap:14px}

/* Footer */
.site-footer{position:absolute;top:1995px;left:0;width:1200px;height:408px;background:var(--footer-bg);color:var(--white)}
.site-footer h4{position:absolute;top:48px;font-size:23px;font-weight:600}
.footer-links{position:absolute;top:106px;font-size:15.5px;line-height:31px}
.contact-item{position:absolute;left:114px;display:flex;align-items:center;gap:14px;font-size:18px;font-weight:500;line-height:26px}
.newsletter-text{position:absolute;left:823px;top:104px;width:270px;font-size:15.5px;line-height:26px}
.newsletter-form{position:absolute;left:823px;top:201px;width:263px;height:37px;display:flex}
.newsletter-form .field{flex:1;background:var(--white);color:#888;font-size:14px;padding:0 11px;display:flex;align-items:center}
.newsletter-form .submit{width:40px;background:var(--accent);display:flex;align-items:center;justify-content:center}
.social{position:absolute;top:311px;left:112px;display:flex;gap:13px}
.social span{width:27px;height:27px;background:var(--white);display:block}
.copyright{position:absolute;top:366px;width:1200px;text-align:center;font-size:15px}
</style>
</head>
<body>

<header class="site-header">
  <div class="brand"><span class="brand-dot"></span><span class="brand-name">Zolvin Data</span></div>
  <nav class="main-nav">
    <a style="left:546px">Home</a>
    <a style="left:623px">About Us</a>
    <a style="left:722px">Our Services</a>
    <a style="left:847px">Rich Connectors</a>
    <a style="left:956px">Support</a>
    <a style="left:1048px">Contact Us</a>
  </nav>
</header>

<section class="hero">
  <div class="hero-bg" role="img" aria-label="Blue digital data background with flowchart boxes and streams of numbers"></div>
  <h1 class="hero-title">Zolvin Data</h1>
  <p class="hero-sub">Enterprise Data Quality and Master<br>Data Management Made Easy</p>
  <div class="slider-arrow prev"><svg width="16" height="16" viewBox="0 0 16 16"><path d="M10 3 L5 8 L10 13" fill="none" stroke="#fff" stroke-width="2"/></svg></div>
  <div class="slider-arrow next"><svg width="16" height="16" viewBox="0 0 16 16"><path d="M6 3 L11 8 L6 13" fill="none" stroke="#fff" stroke-width="2"/></svg></div>
</section>

<div class="stat-card" style="left:114px">
  <svg width="120" height="90" viewBox="0 0 120 90"><path d="M20 44 A40 36 0 1 0 100 44" fill="none" stroke="#1b2a6b" stroke-width="8"/><path d="M8 40 L20 30 L30 44 Z" fill="#1b2a6b"/><text x="47" y="60" font-family="Poppins,sans-serif" font-size="44" font-weight="600" fill="#1b2a6b">5</text><text x="76" y="22" font-family="Poppins,sans-serif" font-size="18" font-weight="600" fill="#1b2a6b">min</text></svg>
  <p>Cleanse addresses<br>in 5 minutes</p>
</div>
<div class="stat-card" style="left:445px">
  <svg width="120" height="90" viewBox="0 0 120 90"><path d="M20 44 A40 36 0 1 0 100 44" fill="none" stroke="#1b2a6b" stroke-width="8"/><path d="M8 40 L20 30 L30 44 Z" fill="#1b2a6b"/><text x="32" y="60" font-family="Poppins,sans-serif" font-size="48" font-weight="600" fill="#1b2a6b">10</text><text x="82" y="22" font-family="Poppins,sans-serif" font-size="18" font-weight="600" fill="#1b2a6b">min</text></svg>
  <p>Match &amp; Merge records<br>in 10 minutes</p>
</div>
<div class="stat-card" style="left:777px">
  <svg width="120" height="90" viewBox="0 0 120 90"><path d="M20 44 A40 36 0 1 0 100 44" fill="none" stroke="#1b2a6b" stroke-width="8"/><path d="M8 40 L20 30 L30 44 Z" fill="#1b2a6b"/><text x="32" y="60" font-family="Poppins,sans-serif" font-size="44" font-weight="600" fill="#1b2a6b">60</text><text x="82" y="22" font-family="Poppins,sans-serif" font-size="18" font-weight="600" fill="#1b2a6b">min</text></svg>
  <p>Master records<br>in 60 minutes</p>
</div>

<section class="service quality">
  <div class="service-bg" role="img" aria-label="Hand touching a glowing security shield within a network of connected points"></div>
  <h2>Data Quality</h2>
  <ul>
    <li><svg width="18" height="16" viewBox="0 0 18 16"><path d="M1 15h2v-3H1zM5 15h2V9H5zM9 15h2V6H9zM13 15h2V2h-2z" fill="#fff"/></svg>Global Address Verification</li>
    <li><svg width="18" height="16" viewBox="0 0 18 16"><path d="M1 15h2v-3H1zM5 15h2V9H5zM9 15h2V6H9zM13 15h2V2h-2z" fill="#fff"/></svg>Data Cleansing/Enrichment</li>
    <li><svg width="18" height="16" viewBox="0 0 18 16"><path d="M1 15h2v-3H1zM5 15h2V9H5zM9 15h2V6H9zM13 15h2V2h-2z" fill="#fff"/></svg>Match and Merge</li>
  </ul>
</section>
<section class="service mdm">
  <div class="service-bg" role="img" aria-label="Folders under a magnifying glass over a blue binary data background"></div>
  <h2>Master Data Management</h2>
  <ul>
    <li><svg width="18" height="16" viewBox="0 0 18 16"><path d="M1 15h2v-3H1zM5 15h2V9H5zM9 15h2V6H9zM13 15h2V2h-2z" fill="#fff"/></svg>Integration</li>
    <li><svg width="18" height="16" viewBox="0 0 18 16"><path d="M1 15h2v-3H1zM5 15h2V9H5zM9 15h2V6H9zM13 15h2V2h-2z" fill="#fff"/></svg>Mastering</li>
    <li><svg width="18" height="16" viewBox="0 0 18 16"><path d="M1 15h2v-3H1zM5 15h2V9H5zM9 15h2V6H9zM13 15h2V2h-2z" fill="#fff"/></svg>Governance</li>
  </ul>
</section>

<section class="connectors">
  <h2>Rich Connectors</h2>
  <div class="connector-card-bg"></div>

  <div class="connector" style="left:130px">
    <div class="icon"><svg width="40" height="40" viewBox="0 0 40 40" fill="none" stroke="#fff" stroke-width="2"><rect x="7" y="4" width="26" height="32" rx="2"/><path d="M12 12h6v6h-6zM22 13h7M22 17h7M12 24h17M12 29h17"/></svg></div>
    <h3>Applications</h3>
    <ul style="padding-left:58px">
      <li><svg width="16" height="16" viewBox="0 0 16 16"><circle cx="8" cy="8" r="6.5" fill="none" stroke="#1b2a6b" stroke-width="1.5"/><path d="M7 5l3 3-3 3" fill="none" stroke="#1b2a6b" stroke-width="1.5"/></svg>Tindlecloud</li>
      <li><svg width="16" height="16" viewBox="0 0 16 16"><circle cx="8" cy="8" r="6.5" fill="none" stroke="#1b2a6b" stroke-width="1.5"/><path d="M7 5l3 3-3 3" fill="none" stroke="#1b2a6b" stroke-width="1.5"/></svg>FieldVane</li>
      <li><svg width="16" height="16" viewBox="0 0 16 16"><circle cx="8" cy="8" r="6.5" fill="none" stroke="#1b2a6b" stroke-width="1.5"/><path d="M7 5l3 3-3 3" fill="none" stroke="#1b2a6b" stroke-width="1.5"/></svg>Corlane</li>
      <li style="white-space:nowrap"><svg width="16" height="16" viewBox="0 0 16 16"><circle cx="8" cy="8" r="6.5" fill="none" stroke="#1b2a6b" stroke-width="1.5"/><path d="M7 5l3 3-3 3" fill="none" stroke="#1b2a6b" stroke-width="1.5"/></svg>Orvane Business Suite</li>
    </ul>
  </div>

  <div class="connector" style="left:355px">
    <div class="icon"><svg width="42" height="42" viewBox="0 0 42 42" fill="none" stroke="#fff" stroke-width="2"><path d="M21 15l6 3v7l-6 3-6-3v-7z"/><path d="M21 4v8M21 31v8M4 21h8M30 21h8M8 8l6 6M34 8l-6 6M8 34l6-6M34 34l-6-6"/></svg></div>
    <h3>Databases</h3>
    <ul style="padding-left:62px">
      <li><svg width="16" height="16" viewBox="0 0 16 16"><circle cx="8" cy="8" r="6.5" fill="none" stroke="#1b2a6b" stroke-width="1.5"/><path d="M7 5l3 3-3 3" fill="none" stroke="#1b2a6b" stroke-width="1.5"/></svg>Orvane DB</li>
      <li><svg width="16" height="16" viewBox="0 0 16 16"><circle cx="8" cy="8" r="6.5" fill="none" stroke="#1b2a6b" stroke-width="1.5"/><path d="M7 5l3 3-3 3" fill="none" stroke="#1b2a6b" stroke-width="1.5"/></svg>Quillbase</li>
      <li style="white-space:nowrap"><svg width="16" height="16" viewBox="0 0 16 16"><circle cx="8" cy="8" r="6.5" fill="none" stroke="#1b2a6b" stroke-width="1.5"/><path d="M7 5l3 3-3 3" fill="none" stroke="#1b2a6b" stroke-width="1.5"/></svg>Halvard SQL Server</li>
      <li><svg width="16" height="16" viewBox="0 0 16 16"><circle cx="8" cy="8" r="6.5" fill="none" stroke="#1b2a6b" stroke-width="1.5"/><path d="M7 5l3 3-3 3" fill="none" stroke="#1b2a6b" stroke-width="1.5"/></svg>Pelican SQL</li>
      <li><svg width="16" height="16" viewBox="0 0 16 16"><circle cx="8" cy="8" r="6.5" fill="none" stroke="#1b2a6b" stroke-width="1.5"/><path d="M7 5l3 3-3 3" fill="none" stroke="#1b2a6b" stroke-width="1.5"/></svg>Corvex DB</li>
    </ul>
  </div>

  <div class="connector" style="left:579px">
    <div class="icon"><svg width="40" height="40" viewBox="0 0 40 40" fill="none" stroke="#fff" stroke-width="2"><path d="M9 4h16l7 7v25H9z"/><circle cx="18" cy="17" r="5"/><path d="M18 12v5h5M14 31l5-5 4 3 6-7"/></svg></div>
    <h3>Files</h3>
    <ul style="padding-left:86px">
      <li><svg width="16" height="16" viewBox="0 0 16 16"><circle cx="8" cy="8" r="6.5" fill="none" stroke="#1b2a6b" stroke-width="1.5"/><path d="M7 5l3 3-3 3" fill="none" stroke="#1b2a6b" stroke-width="1.5"/></svg>CSV</li>
      <li><svg width="16" height="16" viewBox="0 0 16 16"><circle cx="8" cy="8" r="6.5" fill="none" stroke="#1b2a6b" stroke-width="1.5"/><path d="M7 5l3 3-3 3" fill="none" stroke="#1b2a6b" stroke-width="1.5"/></svg>Delimited</li>
      <li><svg width="16" height="16" viewBox="0 0 16 16"><circle cx="8" cy="8" r="6.5" fill="none" stroke="#1b2a6b" stroke-width="1.5"/><path d="M7 5l3 3-3 3" fill="none" stroke="#1b2a6b" stroke-width="1.5"/></svg>Spreadsheet</li>
    </ul>
  </div>

  <div class="connector" style="left:803px">
    <div class="icon"><svg width="40" height="40" viewBox="0 0 40 40" fill="none" stroke="#fff" stroke-width="2"><rect x="6" y="6" width="28" height="28" rx="2"/><path d="M6 14h28M11 10h18M12 20h16v8H12zM15 24h6"/></svg></div>
    <h3>Batch</h3>
    <ul style="padding-left:86px">
      <li style="white-space:nowrap"><svg width="16" height="16" viewBox="0 0 16 16"><circle cx="8" cy="8" r="6.5" fill="none" stroke="#1b2a6b" stroke-width="1.5"/><path d="M7 5l3 3-3 3" fill="none" stroke="#1b2a6b" stroke-width="1.5"/></svg>On your schedule</li>
    </ul>
  </div>
</section>
<div class="carousel-dot prev"><svg width="10" height="10" viewBox="0 0 10 10"><path d="M6.5 1.5L3 5l3.5 3.5" fill="none" stroke="#fff" stroke-width="1.6"/></svg></div>
<div class="carousel-dot next"><svg width="10" height="10" viewBox="0 0 10 10"><path d="M3.5 1.5L7 5l-3.5 3.5" fill="none" stroke="#fff" stroke-width="1.6"/></svg></div>

<section class="cta">
  <p>Lorem ipsum dolor sit amet, consectetur adipiscing elit, sed do eiusmod tempor incididunt ut labore.</p>
  <div class="cta-button"><svg width="28" height="28" viewBox="0 0 28 28" fill="none" stroke="#fff" stroke-width="1.8"><path d="M4 24l6-6M3 15l10-10 10 10-10 10zM10 12l3 3 5-5"/></svg>Support Us</div>
</section>

<footer class="site-footer">
  <h4 style="left:110px">Contact Us</h4>
  <h4 style="left:420px">Quick Links</h4>
  <h4 style="left:601px">Other Links</h4>
  <h4 style="left:823px">Newsletter</h4>

  <div class="contact-item" style="top:108px;align-items:flex-start"><svg width="24" height="32" viewBox="0 0 24 32"><path d="M12 1C6 1 2 5.5 2 11c0 7 10 19 10 19s10-12 10-19C22 5.5 18 1 12 1z" fill="#f5b21b"/><circle cx="12" cy="11" r="4" fill="#2b2b2b"/></svg><span>418 Harbor Line Road<br>Westbrook NJ 07099</span></div>
  <div class="contact-item" style="top:183px"><svg width="32" height="30" viewBox="0 0 32 30" fill="none" stroke="#f5b21b" stroke-width="3"><path d="M5 18v-4a11 11 0 0 1 22 0v4"/><rect x="3" y="17" width="6" height="10" rx="2" fill="#f5b21b"/><rect x="23" y="17" width="6" height="10" rx="2" fill="#f5b21b"/></svg><span>(555) 010-4593</span></div>
  <div class="contact-item" style="top:243px"><svg width="30" height="22" viewBox="0 0 30 22"><rect x="1" y="1" width="28" height="20" rx="2" fill="#f5b21b"/><path d="M2 3l13 10L28 3" fill="none" stroke="#2b2b2b" stroke-width="2"/></svg><span>info@zolvinbyte.example</span></div>

  <ul class="footer-links" style="left:427px">
    <li>Home</li><li>About Us</li><li>Our Services</li><li>Rich Connectors</li><li>Support</li><li>Contact Us</li>
  </ul>
  <ul class="footer-links" style="left:605px">
    <li>Terms &amp; Conditions</li><li>Privacy Policy</li>
  </ul>

  <p class="newsletter-text">But I must explain to you how all this mistaken idea of denouncing pleasure and praising.</p>
  <div class="newsletter-form">
    <div class="field">Enter your email address</div>
    <div class="submit"><svg width="14" height="12" viewBox="0 0 14 12"><path d="M1 6h11M8 2l4 4-4 4" fill="none" stroke="#fff" stroke-width="1.8"/></svg></div>
  </div>

  <div class="social"><span></span><span></span><span></span><span></span></div>
  <p class="copyright">© 2018 Copyrights | All Rights Reserved</p>
</footer>

</body>
</html>
```